Patternmaking service (fashion) card design

I need cards for my patternmaking service. I service both large and small fashion labels including ladies,mens and childrenswear. I would like cards that have a sort of vintage feel, especially 50's and 60's style. Pink is my signature colour. Its important to have a fashion reference of some kind.

Industry/Entity Type

Fashion

Contact Information for Business Card

Marigold Lantern, Patternmaking Service, Pennae Falcastro,
27 Wexbury Lane. Larkmoor Vale. QLD. 4517. 0415836204, email:spoolinda4@quillmail.example. "By appointment only"

```html
<!DOCTYPE html>
<html lang="en">
<head>
<meta charset="utf-8">
<title>Marigold Lantern – Patternmaking Service Cards</title>
<link rel="stylesheet" href="https://fonts.googleapis.com/css2?family=Arvo:wght@400;700&family=Poiret+One&family=Emilys+Candy&display=swap">
<style>
  :root {
    --signature-pink: #e5168a;
    --pink-deep: #c90f74;
    --paper-white: #f7f5f4;
    --backdrop: #e4e2e0;
    --pennant-pale: #f6c9e0;
  }
  * { box-sizing: border-box; margin: 0; padding: 0; }
  html, body { width: 1200px; height: 900px; overflow: hidden; }
  body {
    background: var(--backdrop);
    position: relative;
    font-family: "Arvo", serif;
  }
  .card {
    position: absolute;
    width: 560px;
    height: 320px;
    box-shadow: 0 10px 28px rgba(0,0,0,.22);
    overflow: hidden;
  }
  .card--front { left: 120px; top: 110px; background: var(--signature-pink); color: var(--paper-white); }
  .card--back  { left: 520px; top: 470px; background: var(--paper-white); color: var(--signature-pink); }

  .card__frame {
    position: absolute;
    inset: 22px;
    border: 1.5px solid currentColor;
  }
  .card__corner {
    position: absolute;
    width: 40px;
    height: 40px;
    background: currentColor;
    opacity: .6;
  }
  .card__corner--tl { top: 14px; left: 14px; }
  .card__corner--tr { top: 14px; right: 14px; }
  .card__corner--bl { bottom: 14px; left: 14px; }
  .card__corner--br { bottom: 14px; right: 14px; }

  .brand {
    position: absolute;
    left: 0; right: 0;
    text-align: center;
  }
  .brand__name {
    font-family: "Arvo", serif;
    font-weight: 700;
    font-size: 36px;
    line-height: 1;
  }
  .brand__service {
    display: flex;
    align-items: center;
    justify-content: center;
    gap: 14px;
    margin-top: 10px;
    font-family: "Poiret One", sans-serif;
    font-weight: 400;
    font-size: 19px;
    letter-spacing: 2px;
  }
  .pennant { width: 30px; height: 14px; display: block; }

  .card--front .brand { top: 104px; }
  .front__address {
    position: absolute;
    left: 0; right: 0;
    bottom: 42px;
    text-align: center;
    font-size: 14px;
    font-weight: 700;
    letter-spacing: 1px;
  }

  .card--back .brand { top: 40px; }
  .card--back .brand__name { font-size: 30px; }
  .card--back .brand__service { font-size: 16px; margin-top: 6px; }

  .ribbon {
    position: absolute;
    top: 44px;
    left: -46px;
    width: 230px;
    height: 30px;
    background: var(--signature-pink);
    color: var(--paper-white);
    transform: rotate(-32deg);
    font-size: 11px;
    line-height: 30px;
    text-align: center;
    letter-spacing: 1px;
    font-style: italic;
  }

  .person {
    position: absolute;
    top: 138px;
    left: 0; right: 0;
    text-align: center;
    font-family: "Emilys Candy", cursive;
    font-size: 26px;
    letter-spacing: 2px;
  }
  .contact {
    position: absolute;
    top: 192px;
    left: 0; right: 0;
    text-align: center;
    font-size: 14px;
    font-weight: 700;
    font-style: normal;
    line-height: 1.6;
    letter-spacing: 2px;
  }
  .contact__email { font-weight: 400; }
</style>
</head>
<body>

  <section class="card card--front" aria-label="Business card front">
    <div class="card__frame"></div>
    <div class="card__corner card__corner--tl" role="img" aria-label="Vintage corner flourish"></div>
    <div class="card__corner card__corner--tr" role="img" aria-label="Vintage corner flourish"></div>
    <div class="card__corner card__corner--bl" role="img" aria-label="Vintage corner flourish"></div>
    <div class="card__corner card__corner--br" role="img" aria-label="Vintage corner flourish"></div>

    <div class="brand">
      <h1 class="brand__name">Marigold Lantern</h1>
      <p class="brand__service">
        <svg class="pennant" viewBox="0 0 30 14" aria-hidden="true"><polygon points="0,7 30,0 22,7 30,14" fill="var(--pennant-pale)"/></svg>
        PATTERNMAKING SERVICE
        <svg class="pennant" viewBox="0 0 30 14" aria-hidden="true"><polygon points="30,7 0,0 8,7 0,14" fill="var(--pennant-pale)"/></svg>
      </p>
    </div>

    <p class="front__address">27 Wexbury Lane. Larkmoor Vale. QLD. 4517</p>
  </section>

  <section class="card card--back" aria-label="Business card back">
    <div class="card__frame"></div>
    <div class="card__corner card__corner--tr" role="img" aria-label="Vintage corner flourish"></div>
    <div class="card__corner card__corner--bl" role="img" aria-label="Vintage corner flourish"></div>
    <div class="card__corner card__corner--br" role="img" aria-label="Vintage corner flourish"></div>

    <div class="ribbon">"By appointment only"</div>

    <div class="brand">
      <h2 class="brand__name">Marigold Lantern</h2>
      <p class="brand__service">PATTERNMAKING SERVICE</p>
    </div>

    <p class="person">Pennae Falcastro</p>

    <address class="contact">
      <span>27 Wexbury Lane. Larkmoor Vale. QLD. 4517.</span><br>
      <span>04-1583-6204</span><br>
      <span class="contact__email">spoolinda4@quillmail.example</span>
    </address>
  </section>

</body>
</html>
```